PICTURE CALENDAR - CONSTRUCTION COMPANY

- PICTURES CALENDAR 2018 (wall calendar) - graphic design - square 50 x 50 cm - 14 pages (title - months index pages) - languages ​​- german - Italian - construction industry - minimalistic and clear - modern - for each month inkluding logo color www.tovelbrunn.it
Updates

Project Deadline Extended
Reason: Sehr geehrte Damen und Herren, bitte um eine Fristverlängerung. Es ist Wochenende und ich selbst bekomme auf kein Feedback ob ein Design jetzt passt oder nicht. Weiters haben wir bereits einen Favoriten welcher aber noch Details abändern müsste. Vielen Dank! Mit freundlichen Grüßen, Matthias Kerber

Target Market(s)

construction worker

Industry/Entity Type

Construction

Font styles to use
Sans Serif

Colors
0355a3
dddddd

Requirements
Must have
• 49 x 49 cm 12 months german italiano short image description including logo
Nice to have
• cool line
Should not have
• the graphic design not playful, no gradients

```html
<!DOCTYPE html>
<html lang="de">
<head>
<meta charset="utf-8">
<title>tovel brunn – Wandkalender 2018</title>
<link href="https://fonts.googleapis.com/css2?family=Open+Sans:wght@400;600;700;800&display=swap" rel="stylesheet">
<style>
:root{
  --blue:#1e3f9a;
  --grey-dark:#4a4a4a;
  --ink:#2b2b2b;
  --paper:#ffffff;
  --bg:#dddddd;
  --sunday:#a31d24;
}
*{margin:0;padding:0;box-sizing:border-box}
html,body{width:800px;height:1200px;overflow:hidden;background:var(--bg);font-family:"Open Sans",Arial,sans-serif;color:var(--ink)}
.canvas{position:relative;width:800px;height:1200px}
.page{position:absolute;left:133px;width:536px;height:536px;background:var(--paper);overflow:hidden;box-shadow:2px 3px 6px rgba(0,0,0,.25)}
.page--cover{top:53px}
.page--month{top:617px}
.photo{position:absolute;left:0;top:0;width:536px}
.cover-photo{height:364px;background:linear-gradient(180deg,#dfe3e6 0%,#b9b3a6 30%,#8f8673 55%,#6b5a45 78%,#4e3f30 100%)}
.month-photo{height:262px;background:linear-gradient(180deg,#e4e8ec 0%,#b8b8b0 24%,#5d6e45 40%,#7a8a55 52%,#6fa6a2 62%,#8aa49a 78%,#8d7d5e 100%)}
.band-blue{position:absolute;background:var(--blue)}
.footer{position:absolute;left:0;width:536px;background:var(--grey-dark);color:#fff;font-size:7px;font-weight:700;line-height:9.5px;text-align:center}
.footer .addr,.footer .contact{position:absolute;top:50%;transform:translate(-50%,-50%);white-space:nowrap}
.logo{position:absolute;background:#fff;display:flex;align-items:center;justify-content:center;color:var(--blue);font-weight:800;white-space:nowrap}
.logo .mark{border-radius:50%;background:var(--blue);flex:none}
.logo--cover{left:174px;top:21px;width:195px;height:53px;gap:10px;font-size:22px;letter-spacing:-.5px}
.logo--cover .mark{width:34px;height:34px}
.logo--footer{left:23px;top:8px;width:98px;height:26px;gap:5px;font-size:11px;letter-spacing:-.2px}
.logo--footer .mark{width:16px;height:16px}
.cover-year{position:absolute;left:0;top:394px;width:536px;text-align:center;font-size:60px;font-weight:700;line-height:76px;color:var(--ink)}
.year-box{position:absolute;left:0;top:231px;width:136px;height:54px;background:var(--grey-dark);color:#fff;font-size:37px;font-weight:700;letter-spacing:2px;display:flex;align-items:center;justify-content:center}
.caption{position:absolute;left:144px;top:231px;width:363px;height:19px;background:rgba(60,60,60,.75);color:#fff;font-size:9.5px;font-weight:700;line-height:19px;padding-left:30px;white-space:nowrap}
.month-name{position:absolute;right:27px;top:277px;font-size:19px;font-weight:700;letter-spacing:1.5px;color:var(--blue);white-space:nowrap}
.intro{position:absolute;left:19px;top:311px;width:114px;font-size:7px;font-weight:700;line-height:9.6px;text-align:justify;color:#111}
.grid{position:absolute;left:0;top:0}
.grid span{position:absolute;transform:translate(-50%,-50%);font-size:12.5px;font-weight:700;color:#222;white-space:nowrap}
.grid .dow{color:var(--blue);font-size:11px}
.grid .sun{color:var(--sunday)}
</style>
</head>
<body>
<div class="canvas">

  <section class="page page--cover">
    <div class="photo cover-photo" role="img" aria-label="Tracked loader and excavator working on an alpine construction site below rocky dolomite peaks"></div>
    <div class="logo logo--cover"><span class="mark"></span><span>tovel brunn</span></div>
    <div class="band-blue" style="left:0;top:364px;width:536px;height:10px"></div>
    <div class="cover-year">2018</div>
    <div class="band-blue" style="left:0;top:483px;width:536px;height:8px"></div>
    <footer class="footer" style="top:491px;height:45px">
      <div class="addr" style="left:183px">I-39040 Tovel am Bach, 39040 Tovel al Rio<br>(BZ), Lärchenweg 12, Via Larici</div>
      <div class="contact" style="left:366px">0471 555218<br>@tovelbrunn.it | www.tovelbrunn.it</div>
    </footer>
  </section>

  <section class="page page--month">
    <div class="photo month-photo" role="img" aria-label="Excavator loading a dump truck beside a mountain reservoir, forest and ski lift behind, dolomite peaks on the horizon"></div>
    <div class="caption">LOREM IPSUM DOLOR SIT AMET, CONSECTETUR ADIPISCING ELIT</div>
    <div class="band-blue" style="left:136px;top:252px;width:400px;height:9px"></div>
    <div class="year-box">2018</div>
    <div class="month-name">JÄNNER · GENNAIO</div>
    <p class="intro">Lorem ipsum dolor sit amet, consectetur adipiscing elit, sed do eiusmod tempor incididunt ut labore et dolore magna aliqua.</p>

    <div class="grid">
      <span class="dow" style="left:186px;top:323px">MO | LU</span>
      <span class="dow" style="left:237px;top:323px">DI | MA</span>
      <span class="dow" style="left:289px;top:323px">MI | ME</span>
      <span class="dow" style="left:340px;top:323px">DO | GI</span>
      <span class="dow" style="left:391px;top:323px">FR | VE</span>
      <span class="dow" style="left:442px;top:323px">SA | SA</span>
      <span class="dow" style="left:494px;top:323px">SO | DO</span>

      <span style="left:186px;top:348px">01</span>
      <span style="left:237px;top:348px">02</span>
      <span style="left:289px;top:348px">03</span>
      <span style="left:340px;top:348px">04</span>
      <span style="left:391px;top:348px">05</span>
      <span style="left:442px;top:348px">06</span>
      <span class="sun" style="left:494px;top:348px">07</span>

      <span style="left:186px;top:378px">08</span>
      <span style="left:237px;top:378px">09</span>
      <span style="left:289px;top:378px">10</span>
      <span style="left:340px;top:378px">11</span>
      <span style="left:391px;top:378px">12</span>
      <span style="left:442px;top:378px">13</span>
      <span class="sun" style="left:494px;top:378px">14</span>

      <span style="left:186px;top:408px">15</span>
      <span style="left:237px;top:408px">16</span>
      <span style="left:289px;top:408px">17</span>
      <span style="left:340px;top:408px">18</span>
      <span style="left:391px;top:408px">19</span>
      <span style="left:442px;top:408px">20</span>
      <span class="sun" style="left:494px;top:408px">21</span>

      <span style="left:186px;top:438px">22</span>
      <span style="left:237px;top:438px">23</span>
      <span style="left:289px;top:438px">24</span>
      <span style="left:340px;top:438px">25</span>
      <span style="left:391px;top:438px">26</span>
      <span style="left:442px;top:438px">27</span>
      <span class="sun" style="left:494px;top:438px">28</span>

      <span style="left:186px;top:468px">29</span>
      <span style="left:237px;top:468px">30</span>
      <span style="left:289px;top:468px">31</span>
    </div>

    <div class="band-blue" style="left:0;top:484px;width:536px;height:8px"></div>
    <footer class="footer" style="top:492px;height:44px">
      <div class="logo logo--footer"><span class="mark"></span><span>tovel brunn</span></div>
      <div class="addr" style="left:294px">I-39040 Tovel am Bach, 39040 Tovel al Rio<br>(BZ), Lärchenweg 12, Via Larici</div>
      <div class="contact" style="left:451px">0471 555218<br>@tovelbrunn.it | www.tovelbrunn.it</div>
    </footer>
  </section>

</div>
</body>
</html>
```